Business card design needed for rebranded top-end landscaping business

We need a new business card design, incorporating our logo (colours Green #8dc63f and Grey #8a8c8e) and also some options that include the colour dark navy (eg #000040) as our uniforms are navy with white and grey trim.

We are an innovative landscaping company that maintains high-end gardens for meticulous clients. We pride ourselves on our customer service, our professionalism, and our workmanship.

Our business name needs to be easily read and our branding needs to be bold and memorable, without screaming "tradesman"! We prefer clean lines over lots of fine detail.

The design MUST include:
- Business name ("Brindlemere Gardening")
- Logo (file uploaded)
- Employee name
- Phone number
- Email address
- www.brindlemeregardening.com.au
- Social A & Social B logos
- The Turfcraft Guild logo (file uploaded) along with the word "Member"
- Licence "Lic. 871396K"

OPTIONAL inclusions:
- "Creating outdoor spaces for our community to be inspired, refreshed and re-energised"
- "Landscape Maintenance - Irrigation - Arboriculture" (dashes can be replaced with dots or other)
- "Fully qualified, licensed & insured"
- "Residential - Strata - Commercial - Real Estate" (dashes can be replaced with dots or other)

Target Market(s)

High-end professionals and retirees, real estate agents

Industry/Entity Type

Landscaping

Contact Information for Business Card

See Project description

Font styles to use
Sans Serif

Colors

Designer to choose colors to be used in the design.

Requirements
Must have
• Must incorporate our logo, and colours Green #8dc63f and Grey #8a8c8e) from the logo, and the colour DARK NAVY (eg #000040).
• The design MUST include:
• - Business name ("Brindlemere Gardening")
• - Logo (file uploaded)
• - Employee name
• - Phone number
• - Email address
• - www.brindlemeregardening.com.au
• - Social A & Social B logos
• - The Turfcraft Guild logo (file uploaded) along with the word "Member"
• - Licence "Lic. 871396K"
Nice to have
• OPTIONAL inclusions:
• - "Creating outdoor spaces for our community to be inspired, refreshed and re-energised"
• - "Landscape Maintenance - Irrigation - Arboriculture" (dashes can be replaced with dots or other)
• - "Fully qualified, licensed & insured"
• - "Residential - Strata - Commercial - Real Estate" (dashes can be replaced with dots or other)

```html
<!DOCTYPE html>
<html lang="en">
<head>
<meta charset="utf-8">
<title>Brindlemere Gardening – Business Card</title>
<link rel="stylesheet" href="https://fonts.googleapis.com/css2?family=Lato:wght@400;700;900&display=swap">
<style>
  :root {
    --green: #8dc63f;
    --grey: #8a8c8e;
    --navy: #0d0f45;
    --navy-soft: #171b55;
    --ink: #2b2b2b;
    --paper: #ffffff;
    --backdrop: #e6e7ea;
  }
  * { box-sizing: border-box; margin: 0; padding: 0; }
  html, body { width: 1200px; height: 900px; overflow: hidden; }
  body {
    background: var(--backdrop);
    font-family: "Lato", Arial, sans-serif;
    position: relative;
  }
  .card {
    position: absolute;
    width: 700px;
    height: 400px;
    border-radius: 18px;
    overflow: hidden;
    box-shadow: 0 10px 30px rgba(0,0,0,.18);
  }

  /* Back side */
  .card--back { left: 70px; top: 40px; background: var(--paper); text-align: center; }
  .guild {
    margin-top: 50px;
    display: flex; flex-direction: column; align-items: center;
  }
  .guild__name {
    font-size: 34px; font-weight: 700; letter-spacing: 3px;
    color: var(--ink); text-transform: uppercase;
  }
  .guild__member {
    display: flex; align-items: center; gap: 10px;
    margin-top: 6px; font-size: 13px; letter-spacing: 2px; color: var(--ink);
  }
  .guild__member::before, .guild__member::after {
    content: ""; width: 90px; height: 1px; background: var(--ink);
  }
  .tagline {
    margin: 30px auto 0; width: 520px;
    font-size: 21px; line-height: 1.25; color: var(--green);
  }
  .services {
    margin-top: 18px; font-size: 19px; color: var(--ink);
    display: flex; justify-content: center; flex-wrap: wrap; gap: 6px 14px;
  }
  .services li { list-style: none; display: flex; align-items: center; gap: 6px; }
  .services li::before {
    content: ""; width: 11px; height: 11px; border-radius: 50%; background: var(--green);
  }
  .qualified { margin-top: 22px; font-size: 20px; color: var(--green); }
  .services--sectors { margin-top: 12px; }

  /* Front side */
  .card--front { left: 430px; top: 470px; background: var(--navy); color: var(--paper); }
  .watermark {
    position: absolute; right: -60px; top: -30px;
    width: 400px; height: 400px; border-radius: 50%;
    background: var(--navy-soft);
  }
  .person {
    position: absolute; left: 0; top: 40px;
    padding-left: 44px; border-left: 24px solid var(--green);
  }
  .person__name { font-size: 38px; font-weight: 900; color: var(--green); line-height: 1; }
  .person__role { font-size: 18px; color: #c9cad6; margin-top: 6px; }
  .brand {
    position: absolute; right: 40px; top: 120px; width: 270px;
    display: flex; flex-direction: column; align-items: center; gap: 10px;
  }
  .brand__mark { width: 56px; height: 56px; border-radius: 50%; background: var(--grey); }
  .brand__name {
    font-size: 30px; font-weight: 700; color: var(--grey);
    text-align: center; line-height: 1.1;
  }
  .contact { position: absolute; left: 68px; top: 190px; }
  .contact__company { font-size: 18px; font-weight: 700; color: var(--green); margin-bottom: 10px; }
  .contact__row {
    display: flex; align-items: center; gap: 12px;
    font-size: 16px; color: #e4e5ee; margin-bottom: 6px;
  }
  .contact__row svg { width: 18px; height: 18px; flex: none; }
  .licence { font-size: 26px; color: var(--green); margin-top: 14px; }
  .rule {
    position: absolute; left: 40px; right: 40px; bottom: 26px;
    height: 1px; background: rgba(255,255,255,.25);
  }
  .social {
    position: absolute; right: 40px; bottom: 44px;
    display: flex; gap: 16px; font-size: 13px; color: var(--paper);
  }
  .social span { display: flex; align-items: center; gap: 6px; }
  .social span::before {
    content: ""; width: 18px; height: 18px; border-radius: 3px; background: var(--paper);
  }
</style>
</head>
<body>

<section class="card card--back">
  <div class="guild">
    <div class="guild__name">The Turfcraft Guild</div>
    <div class="guild__member">MEMBER</div>
  </div>
  <p class="tagline">"Creating outdoor spaces for our community to be inspired, refreshed and re-energised"</p>
  <ul class="services">
    <li>Landscape Maintenance</li><li>Irrigation</li><li>Arboriculture</li>
  </ul>
  <p class="qualified">Fully qualified, licensed &amp; insured</p>
  <ul class="services services--sectors">
    <li>Residential</li><li>Strata</li><li>Commercial</li><li>Real Estate</li>
  </ul>
</section>

<section class="card card--front">
  <div class="watermark" aria-hidden="true"></div>
  <div class="person">
    <div class="person__name">ELLIOT MARSH</div>
    <div class="person__role">Founder &amp; Director</div>
  </div>
  <div class="brand">
    <div class="brand__mark" aria-hidden="true"></div>
    <div class="brand__name">Brindlemere Gardening</div>
  </div>
  <div class="contact">
    <div class="contact__company">Brindlemere Gardening Inc</div>
    <div class="contact__row">
      <svg viewBox="0 0 24 24" fill="#8dc63f"><path d="M6.6 10.8a15 15 0 0 0 6.6 6.6l2.2-2.2a1 1 0 0 1 1-.25 11.4 11.4 0 0 0 3.6.57 1 1 0 0 1 1 1V20a1 1 0 0 1-1 1A17 17 0 0 1 3 4a1 1 0 0 1 1-1h3.5a1 1 0 0 1 1 1c0 1.25.2 2.45.57 3.57a1 1 0 0 1-.25 1z"/></svg>
      0412 558 903
    </div>
    <div class="contact__row">
      <svg viewBox="0 0 24 24" fill="none" stroke="#8dc63f" stroke-width="2"><rect x="3" y="5" width="18" height="14" rx="1"/><path d="M3 6l9 7 9-7"/></svg>
      info@brindlemeregardening.com.au
    </div>
    <div class="contact__row">
      <svg viewBox="0 0 24 24" fill="none" stroke="#8dc63f" stroke-width="2"><circle cx="12" cy="12" r="9"/><path d="M3 12h18M12 3c3 3 3 15 0 18M12 3c-3 3-3 15 0 18"/></svg>
      www.brindlemeregardening.com.au
    </div>
    <div class="licence">Lic. 871396K</div>
  </div>
  <div class="social"><span>Social A</span><span>Social B</span></div>
  <div class="rule"></div>
</section>

</body>
</html>
```